Northfield Ledger Business Card

Business card with QR Code for an accounting and tax business

Target Market(s)

Small Business and Individual Tax

Industry/Entity Type

Bookkeeping, Accounting and Taxes

Contact Information for Business Card

482 WILLOWMERE ST STE 2406 #718342 BOSTON, MA Zip: 02139

Requirements
Must have
• Name and Address

```html
<!DOCTYPE html>
<html lang="en">
<head>
<meta charset="utf-8">
<title>Northfield Ledger Business Card</title>
<link href="https://fonts.googleapis.com/css2?family=Libre+Baskerville:wght@400;700&family=Arimo:wght@400&display=swap" rel="stylesheet">
<style>
  :root {
    --backdrop: #3a3a3a;
    --card-dark: #1c1c1c;
    --card-dark-ink: #2b2b2b;
    --card-light: #f7f7f7;
    --ink: #1e1e1e;
    --ink-soft: #6d6d6d;
    --rule: #b9b9b9;
  }
  * { margin: 0; padding: 0; box-sizing: border-box; }
  html, body { width: 1200px; height: 689px; overflow: hidden; }
  body {
    background: var(--backdrop);
    display: flex;
    align-items: center;
    justify-content: center;
    gap: 60px;
  }
  .card {
    width: 510px;
    height: 292px;
    border-radius: 18px;
    position: relative;
  }
  .card-front {
    background: var(--card-dark);
    display: flex;
    align-items: center;
    justify-content: center;
    gap: 18px;
  }
  .front-mark {
    width: 54px; height: 54px;
    border: 3px solid var(--card-dark-ink);
    border-radius: 50%;
  }
  .front-name {
    font-family: "Libre Baskerville", serif;
    font-weight: 700;
    font-size: 30px;
    color: var(--card-dark-ink);
  }
  .card-back {
    background: var(--card-light);
    display: flex;
    align-items: center;
    padding: 0 30px;
  }
  .brand {
    width: 215px;
    display: flex;
    flex-direction: column;
    align-items: center;
    gap: 10px;
  }
  .brand-mark {
    width: 46px; height: 46px;
    border: 3px solid var(--ink);
    border-radius: 50%;
  }
  .brand-name {
    font-family: "Libre Baskerville", serif;
    font-weight: 700;
    font-size: 22px;
    color: var(--ink);
    border-top: 1.5px solid var(--ink);
    border-bottom: 1.5px solid var(--ink);
    padding: 5px 4px;
    white-space: nowrap;
  }
  .divider {
    width: 1px;
    height: 150px;
    background: var(--rule);
    margin: 0 22px 0 8px;
  }
  .details { font-family: "Arimo", sans-serif; color: var(--ink); }
  .person-name {
    font-family: "Libre Baskerville", serif;
    font-weight: 700;
    font-size: 17px;
    letter-spacing: 0.3px;
  }
  .person-title { font-size: 11px; color: var(--ink-soft); margin-bottom: 12px; }
  .address { font-size: 12px; line-height: 1.35; margin-bottom: 12px; }
  .contacts { list-style: none; font-size: 12px; line-height: 1.45; }
  .contacts li { display: flex; align-items: center; gap: 7px; }
  .contacts svg { width: 10px; height: 10px; fill: var(--ink); flex: none; }
</style>
</head>
<body>
  <div class="card card-front">
    <span class="front-mark"></span>
    <span class="front-name">Northfield Ledger</span>
  </div>

  <div class="card card-back">
    <div class="brand">
      <span class="brand-mark"></span>
      <span class="brand-name">Northfield Ledger</span>
    </div>
    <div class="divider"></div>
    <div class="details">
      <div class="person-name">DANIEL FOSTER</div>
      <div class="person-title">Managing Director</div>
      <div class="address">482 Willowmere St Ste 2406<br>#718342 Boston, MA Zip: 02139</div>
      <ul class="contacts">
        <li><svg viewBox="0 0 10 10"><path d="M2 0.5 L3.6 0.5 L4.2 2.8 L3 3.6 Q4 6 6.4 7 L7.2 5.8 L9.5 6.4 L9.5 8 Q9.5 9.5 8 9.5 Q0.5 8.5 0.5 2 Q0.5 0.5 2 0.5Z"/></svg>617-555-0142</li>
        <li><svg viewBox="0 0 10 10"><path d="M2.5 0 H7.5 Q8 0 8 0.5 V9.5 Q8 10 7.5 10 H2.5 Q2 10 2 9.5 V0.5 Q2 0 2.5 0Z M3 1 V8 H7 V1Z"/></svg>617-555-0187</li>
        <li><svg viewBox="0 0 10 10"><path d="M0 2 H10 V8.5 H0Z M0.8 2.6 L5 5.6 L9.2 2.6 V2.6 Z" fill-rule="evenodd"/></svg>hello@northfieldledger.com</li>
        <li><svg viewBox="0 0 10 10"><circle cx="5" cy="5" r="4.8"/></svg>www.northfieldledger.com</li>
      </ul>
    </div>
  </div>
</body>
</html>
```